Copperleaf Motorized Shade Business Card

Hello, we've had our logo made. Now we are looking for a clean and cool looking business card. One side can just be the logo with any design elements that might look good with it. The other side will be Name, Phone Number and Email. There will not be an address on the card.

```html
<!DOCTYPE html>
<html lang="en">
<head>
<meta charset="UTF-8">
<title>Copperleaf Motorized Shade – Business Card</title>
<link rel="stylesheet" href="https://fonts.googleapis.com/css2?family=Montserrat:wght@500;700;800&display=swap">
<style>
  :root {
    --stage: #2b2b2d;
    --card: #033a78;
    --card-edge: #022c5e;
    --accent: #1fb0ec;
    --white: #ffffff;
  }
  * { box-sizing: border-box; margin: 0; padding: 0; }
  html, body {
    width: 1200px;
    height: 960px;
    overflow: hidden;
    background: var(--stage);
    font-family: "Montserrat", sans-serif;
  }
  .canvas {
    position: relative;
    width: 1200px;
    height: 960px;
  }
  .card {
    position: absolute;
    width: 760px;
    height: 434px;
    background: var(--card);
    border-radius: 4px;
    box-shadow: 0 0 0 1px var(--card-edge), 0 18px 40px rgba(0,0,0,.45);
    overflow: hidden;
  }
  .card--front { left: 80px; top: 40px; }
  .card--back  { left: 360px; top: 486px; }

  .brand {
    display: flex;
    align-items: center;
    gap: 14px;
    color: var(--white);
    font-weight: 800;
  }
  .brand__mark {
    width: 22px;
    height: 22px;
    background: var(--accent);
    flex: none;
  }
  .brand__name {
    display: flex;
    flex-direction: column;
    line-height: 1.05;
  }
  .brand__title { text-transform: uppercase; letter-spacing: .02em; }
  .brand__tag { text-transform: uppercase; letter-spacing: .22em; }

  .card--front .brand {
    position: absolute;
    left: 50%;
    top: 50%;
    transform: translate(-50%, -50%);
  }
  .card--front .brand__title { font-size: 58px; }
  .card--front .brand__tag { font-size: 19px; margin-top: 8px; }

  .card--back .brand {
    position: absolute;
    left: 70px;
    top: 250px;
  }
  .card--back .brand__mark { width: 16px; height: 16px; }
  .card--back .brand__title { font-size: 34px; }
  .card--back .brand__tag { font-size: 11px; margin-top: 6px; }

  .divider {
    position: absolute;
    left: 400px;
    top: 150px;
    width: 2px;
    height: 150px;
    background: var(--accent);
  }
  .contact {
    position: absolute;
    left: 430px;
    top: 150px;
    color: var(--white);
  }
  .contact__name {
    color: var(--accent);
    font-weight: 800;
    font-size: 24px;
    letter-spacing: .02em;
    text-transform: uppercase;
  }
  .contact__role {
    font-weight: 500;
    font-size: 15px;
    margin-top: 4px;
  }
  .contact__list {
    list-style: none;
    margin-top: 22px;
  }
  .contact__item {
    display: flex;
    align-items: center;
    gap: 10px;
    font-size: 15px;
    font-weight: 500;
    margin-bottom: 8px;
  }
  .contact__icon { width: 16px; height: 16px; flex: none; }
</style>
</head>
<body>
<main class="canvas">

  <section class="card card--front" aria-label="Card front">
    <div class="brand">
      <span class="brand__mark"></span>
      <div class="brand__name">
        <span class="brand__title">Copperleaf</span>
        <span class="brand__tag">Motorized Shade</span>
      </div>
    </div>
  </section>

  <section class="card card--back" aria-label="Card back">
    <div class="brand">
      <span class="brand__mark"></span>
      <div class="brand__name">
        <span class="brand__title">Copperleaf</span>
        <span class="brand__tag">Motorized Shade</span>
      </div>
    </div>

    <div class="divider"></div>

    <div class="contact">
      <h1 class="contact__name">Daniel Rowe</h1>
      <p class="contact__role">General Manager</p>
      <ul class="contact__list">
        <li class="contact__item">
          <svg class="contact__icon" viewBox="0 0 16 16" aria-hidden="true">
            <path d="M3.5 1.5l2.5 3-1.5 1.8c.8 1.8 2.2 3.2 4 4l1.8-1.5 3 2.5-1.6 2.2C6.5 13.5 2.5 9.5 1.3 3.1z" fill="var(--accent)"/>
          </svg>
          <span>+243 970 555 210</span>
        </li>
        <li class="contact__item">
          <svg class="contact__icon" viewBox="0 0 16 16" aria-hidden="true">
            <rect x="1" y="3" width="14" height="10" rx="1" fill="var(--accent)"/>
            <path d="M1.5 3.8L8 9l6.5-5.2" fill="none" stroke="var(--card)" stroke-width="1.3"/>
          </svg>
          <span>info@copperleafshades.com</span>
        </li>
        <li class="contact__item">
          <svg class="contact__icon" viewBox="0 0 16 16" aria-hidden="true">
            <circle cx="8" cy="8" r="7" fill="var(--accent)"/>
            <path d="M1 8h14M8 1c-2.5 2.5-2.5 11.5 0 14M8 1c2.5 2.5 2.5 11.5 0 14" fill="none" stroke="var(--card)" stroke-width="1"/>
          </svg>
          <span>www.copperleafshades.com</span>
        </li>
      </ul>
    </div>
  </section>

</main>
</body>
</html>
```